Professional, Attractive, Simple Website Needed!!

We completed the design for our logo.

We need a website built out around this.

Here are a couple samples of how we want ours formatted.

http://brvtawatt.com

http://www.brightmerlo.com/lp/free-quote?LeadSource=Search%20Engine&ProgramName=webfind&experience=qual&language=en&type=brd&gclid=Xq7LMnvrTPKDWQAbZeRFtoPLmNcGxJbYTUWoKdMvCeWsfRgHyZnXpLoKqwErTyUiOpAsDfGhJkLzXcVb_zxwQ

http://qmorel.co

Project Deadline Extended
Reason: Extending this deadline due to our delay in providing designers with content for each page. This is coming in next 24 hours.

Project Deadline Extended
Reason: Due to scheduling conflicts and extended travel delays related to Puerto Rico, the deadline has been extended. Your patience is greatly appreciated.

Project Deadline Extended
Reason: Travel and scheduling conflicts have made it impossible to give this project the thorough review it deserves, therefore I am extending the deadline. Thank you for your patience!

Target Market(s)

Home Owners who earn 60k + household annually

Industry/Entity Type

It Professional

Coding

Coded - Design and coding required

Number of Pages Required

5+ page

Font styles to use
Serif

Colors
34a7d8
9bcb3c

Requirements
Must have
• Simple
• Lead form Entry (Ability for visitor to enter Name, number and address for a quote)
• Sleek Design
• Professional
• Testimonials
• Use color Scheme of Design Logo Attached
Nice to have
• Video when site starts
• Like this
• https://www.clipvault.com/watch?v=Rk8TpQwZmNe&feature=clipv.lt
Should not have
• Should not include Commercial solar
• Should not include wind power

```html
<!DOCTYPE html>
<html lang="en">
<head>
<meta charset="utf-8">
<title>Terravolt Energy</title>
<link href="https://fonts.googleapis.com/css2?family=Open+Sans:ital,wght@0,400;0,600;0,700;0,800;1,400&display=swap" rel="stylesheet">
<style>
  :root {
    --blue: #34a7d8;
    --green: #9bcb3c;
    --dark: #2b2b2b;
    --ink: #333333;
    --muted: #555555;
    --card: #f3f4f5;
    --white: #ffffff;
  }
  * { margin: 0; padding: 0; box-sizing: border-box; }
  html, body { width: 880px; height: 1200px; overflow: hidden; background: var(--white); }
  body { font-family: "Open Sans", sans-serif; color: var(--ink); }
  .page { position: relative; width: 880px; height: 1200px; overflow: hidden; }

  /* Hero */
  .hero { position: absolute; left: 0; top: 0; width: 880px; height: 400px; overflow: hidden; }
  .hero-photo {
    position: absolute; inset: 0;
    background: linear-gradient(180deg, #3f6f9c 0%, #7fa8c9 30%, #b9cfdf 55%, #5c87b3 72%, #2f5d92 100%);
  }
  .hero-globe {
    position: absolute; left: 220px; top: 70px; width: 440px; height: 440px; border-radius: 50%;
    background: radial-gradient(circle at 45% 40%, #5a8fb8 0%, #2d5f86 45%, #23486a 70%, #4d7a3a 100%);
  }
  .hero-curve { position: absolute; left: 0; top: 300px; width: 880px; height: 100px; }

  .brand { position: absolute; left: 46px; top: 36px; display: flex; align-items: center; gap: 8px; }
  .brand-dot { width: 14px; height: 14px; border-radius: 50%; background: var(--white); }
  .brand-name { font-size: 13px; font-weight: 600; color: var(--white); letter-spacing: .5px; text-transform: uppercase; }

  .nav { position: absolute; left: 354px; top: 38px; display: flex; gap: 4px; }
  .nav a { display: block; padding: 5px 9px; font-size: 8.5px; font-weight: 700; color: var(--white); text-decoration: none; letter-spacing: .3px; }
  .nav a.active { background: var(--green); }
  .phone { position: absolute; left: 700px; top: 40px; display: flex; align-items: center; gap: 9px; font-size: 14px; font-weight: 700; color: var(--blue); }

  .hero-title { position: absolute; left: 0; top: 154px; width: 880px; text-align: center; font-size: 39px; line-height: 39px; font-weight: 800; color: var(--white); letter-spacing: 1px; text-shadow: 0 2px 4px rgba(0,0,0,.35); }
  .play { position: absolute; left: 414px; top: 247px; }
  .play-label { position: absolute; left: 0; top: 305px; width: 880px; text-align: center; font-size: 12.5px; font-weight: 700; color: var(--white); text-decoration: underline; letter-spacing: .5px; }

  /* Quote form */
  .quote { position: absolute; left: 220px; top: 359px; width: 442px; height: 128px; background: var(--dark); border: 3px solid #d9d9d9; padding: 0 11px; }
  .quote h2 { text-align: center; font-size: 17px; font-weight: 700; color: var(--white); letter-spacing: .5px; margin-top: 11px; }
  .quote-fields { display: flex; gap: 5px; margin-top: 8px; }
  .quote-field { flex: 1; height: 26px; background: var(--white); border-radius: 2px; font-size: 8.5px; color: var(--muted); padding: 8px 9px; }
  .quote-submit { margin-top: 7px; height: 26px; background: var(--green); color: var(--white); font-size: 10.5px; font-weight: 700; text-align: center; line-height: 26px; letter-spacing: .5px; border-radius: 2px; }

  /* About band */
  .about { position: absolute; left: 0; top: 522px; width: 880px; height: 214px; background: var(--blue); text-align: center; color: var(--white); }
  .about h2 { font-size: 19px; font-weight: 700; letter-spacing: .7px; margin-top: 29px; }
  .about p { width: 730px; margin: 13px auto 0; font-size: 10.4px; line-height: 17px; }
  .btn-more { display: inline-block; margin-top: 18px; width: 109px; height: 30px; line-height: 30px; background: var(--green); font-size: 10px; font-weight: 700; letter-spacing: .5px; }

  /* Testimonials */
  .testimonials-title { position: absolute; left: 0; top: 767px; width: 880px; text-align: center; font-size: 19px; font-weight: 700; color: var(--ink); letter-spacing: .7px; }
  .testimonial { position: absolute; top: 808px; width: 243px; }
  .testimonial-card { position: relative; height: 138px; background: linear-gradient(180deg, #eeeff0, #f6f7f7); padding: 22px 18px 0; text-align: center; font-size: 10px; line-height: 15px; font-style: italic; color: var(--ink); }
  .quote-open, .quote-close { position: absolute; font-family: "Open Sans", sans-serif; font-size: 54px; font-weight: 800; font-style: normal; color: var(--green); line-height: 1; }
  .quote-open { left: 7px; top: 2px; }
  .quote-close { right: 14px; top: 94px; }
  .testimonial-text { position: relative; }
  .avatar { position: absolute; left: 96px; top: 113px; width: 50px; height: 50px; border-radius: 50%; border: 2px solid #e3e3e3; background: linear-gradient(180deg, #d8dde2, #a9b2bb); }
  .testimonial-name { margin-top: 36px; text-align: center; font-size: 10.5px; font-weight: 700; color: var(--blue); letter-spacing: .4px; }
  .testimonial-location { text-align: center; font-size: 9.5px; font-style: italic; color: var(--ink); margin-top: 2px; }

  /* Footer */
  .footer { position: absolute; left: 0; top: 1074px; width: 880px; height: 126px; background: var(--green); }
  .footer-brand { position: absolute; left: 0; top: 1050px; width: 880px; display: flex; flex-direction: column; align-items: center; }
  .footer-badge { width: 44px; height: 44px; border-radius: 50%; background: var(--white); border: 3px solid var(--green); }
  .footer-name { margin-top: 4px; font-size: 11px; font-weight: 600; color: var(--white); letter-spacing: .5px; text-transform: uppercase; }
  .copyright { position: absolute; left: 0; top: 1127px; width: 880px; text-align: center; font-size: 9.5px; color: var(--white); }
  .social { position: absolute; left: 346px; top: 1152px; display: flex; gap: 23px; }
  .social span { width: 20px; height: 20px; border-radius: 50%; background: var(--white); }
</style>
</head>
<body>
<div class="page">

  <header class="hero">
    <div class="hero-photo" role="img" aria-label="Photo of wind turbines and solar panels under a cloudy blue sky"></div>
    <div class="hero-globe" role="img" aria-label="Image of planet Earth rising over a green field"></div>
    <svg class="hero-curve" viewBox="0 0 880 100" preserveAspectRatio="none" aria-hidden="true">
      <path d="M0 96 Q440 50 880 96 L880 100 L0 100 Z" fill="#ffffff"/>
    </svg>

    <div class="brand"><span class="brand-dot"></span><span class="brand-name">Terravolt Energy</span></div>

    <nav class="nav">
      <a class="active">HOME</a>
      <a>ABOUT</a>
      <a>WHY US?</a>
      <a>HOW IT WORKS</a>
      <a>CONTACT US</a>
    </nav>

    <div class="phone">
      <svg width="12" height="12" viewBox="0 0 24 24" aria-hidden="true"><path fill="#34a7d8" d="M6.6 10.8a15.1 15.1 0 0 0 6.6 6.6l2.2-2.2c.3-.3.7-.4 1-.2 1.1.4 2.3.6 3.6.6.6 0 1 .4 1 1V20c0 .6-.4 1-1 1A17 17 0 0 1 3 4c0-.6.4-1 1-1h3.5c.6 0 1 .4 1 1 0 1.3.2 2.5.6 3.6.1.3 0 .7-.2 1z"/></svg>
      <span>1-800-555-0148</span>
    </div>

    <h1 class="hero-title">WELCOME TO<br>TERRAVOLT ENERGY</h1>
    <svg class="play" width="52" height="52" viewBox="0 0 52 52" aria-label="Play video">
      <circle cx="26" cy="26" r="23" fill="none" stroke="#ffffff" stroke-width="4"/>
      <path d="M20 15 L37 26 L20 37 Z" fill="#ffffff"/>
    </svg>
    <div class="play-label">PLAY VIDEO</div>
  </header>

  <form class="quote">
    <h2>REQUEST A QUOTE</h2>
    <div class="quote-fields">
      <div class="quote-field">Enter Name</div>
      <div class="quote-field">Phone No.</div>
      <div class="quote-field">Email Address</div>
    </div>
    <div class="quote-submit">SUBMIT</div>
  </form>

  <section class="about">
    <h2>WELCOME TO OUR WEBSITE</h2>
    <p>Aliquam molestie, mi et imperdiet euismod, dui purus auctor tellus, et interdum lacus lectus et ante. Sed accumsan sollicitudin sapien, sit amet adipiscing turpis gravida ac. In congue, neque ac lobortis volutpat, libero mauris varius mi, vitae suscipit ipsum ligula vitae risus. Duis aliquam nibh a dui iaculis viverra id a velit. Vivamus egestas risus in magna varius commodo. Sed semper viverra egestas. Etiam pretium porttitor lectus, vel ornare neque porta volutpat.</p>
    <span class="btn-more">READ MORE</span>
  </section>

  <h2 class="testimonials-title">TESTIMONIALS</h2>

  <article class="testimonial" style="left:54px">
    <div class="testimonial-card">
      <span class="quote-open">&ldquo;</span><span class="quote-close">&rdquo;</span>
      <p class="testimonial-text">Lorem ipsum dolor sit amet, consect- etuer adipiscing elit, sed diam nonummy nibh euismod tincidunt ut laoreet dolore magna aliquam erat volutpat. Ut wisi enim ad minim veniam quis....</p>
      <div class="avatar" role="img" aria-label="Portrait photo of a customer"></div>
    </div>
    <div class="testimonial-name">NAME HEADING</div>
    <div class="testimonial-location">Location</div>
  </article>

  <article class="testimonial" style="left:318px">
    <div class="testimonial-card">
      <span class="quote-open">&ldquo;</span><span class="quote-close">&rdquo;</span>
      <p class="testimonial-text">Lorem ipsum dolor sit amet, consect- etuer adipiscing elit, sed diam nonummy nibh euismod tincidunt ut laoreet dolore magna aliquam erat volutpat. Ut wisi enim ad minim veniam quis....</p>
      <div class="avatar" role="img" aria-label="Portrait photo of a customer"></div>
    </div>
    <div class="testimonial-name">NAME HEADING</div>
    <div class="testimonial-location">Location</div>
  </article>

  <article class="testimonial" style="left:584px">
    <div class="testimonial-card">
      <span class="quote-open">&ldquo;</span><span class="quote-close">&rdquo;</span>
      <p class="testimonial-text">Lorem ipsum dolor sit amet, consect- etuer adipiscing elit, sed diam nonummy nibh euismod tincidunt ut laoreet dolore magna aliquam erat volutpat. Ut wisi enim ad minim veniam quis....</p>
      <div class="avatar" role="img" aria-label="Portrait photo of a customer"></div>
    </div>
    <div class="testimonial-name">NAME HEADING</div>
    <div class="testimonial-location">Location</div>
  </article>

  <footer class="footer"></footer>
  <div class="footer-brand">
    <span class="footer-badge"></span>
    <span class="footer-name">Terravolt Energy</span>
  </div>
  <div class="copyright">Copyright © 2017. Company Name. All Right Reserved</div>
  <div class="social" aria-label="Social media links">
    <span></span><span></span><span></span><span></span><span></span>
  </div>

</div>
</body>
</html>
```